IT Consulting Business needs a web design

We need a web design for an IT Consulting company called "Vornelix". We want to replace the existing web site (www.vornelix-example.com) with a new design. Our services are IT Consulting, IT Training, IT Outsourcing.
We would like to see designs that communicate "Trusted IT Advisor" with modern & bold design.

We would like to see the design of 2 pages:
1. Home page (www.vornelix-example.com)
2. The detail page (http://www.vornelix-example.com/index_files/consulting.htm)

Industry/Entity Type

Business

```html
<!DOCTYPE html>
<html lang="en">
<head>
<meta charset="utf-8">
<title>Vornelix – IT Consulting Company</title>
<link rel="stylesheet" href="https://fonts.googleapis.com/css2?family=Raleway:wght@400;500;700;800&family=Arimo:ital,wght@0,400;0,700;1,400&display=swap">
<style>
:root{
  --red:#b3141b;
  --red-dark:#8e0b10;
  --ink:#222;
  --body:#333;
  --muted:#555;
  --light-bg:#efefef;
  --bar-dark:#1c1c1c;
  --bar-mid:#3a3a3a;
  --blue-deep:#0f4d95;
  --blue:#2a78c6;
  --white:#fff;
  --frame:#dcdcdc;
  --rule:#cfcfcf;
}
*{margin:0;padding:0;box-sizing:border-box}
html,body{width:1200px;height:1112px;overflow:hidden}
body{position:relative;background:var(--white);font-family:"Arimo",Arial,sans-serif;color:var(--body)}
.abs{position:absolute}

/* top bar */
.top-bar{left:0;top:0;width:1200px;height:54px;background:linear-gradient(#2b2b2b,var(--bar-dark));border-top:4px solid #d9d9d9}
.nav a{position:absolute;top:22px;color:var(--white);font-size:14px;text-decoration:none;transform:translateX(-50%);white-space:nowrap}
.nav .active-tab{position:absolute;left:495px;top:4px;width:77px;height:58px;background:var(--red)}
.nav .active-tab::before,.nav .active-tab::after{content:"";position:absolute;top:50px;border-top:8px solid var(--red-dark);}
.nav .active-tab::before{left:-9px;border-left:9px solid transparent}
.nav .active-tab::after{right:-9px;border-right:9px solid transparent}

/* logo card */
.logo-card{left:108px;top:0;width:254px;height:106px;background:linear-gradient(#fff,#e6e6e6);border-radius:0 0 12px 12px;box-shadow:0 6px 10px rgba(0,0,0,.35);z-index:3}
.brand-name{font-family:"Raleway",sans-serif;font-weight:500;color:var(--red);font-size:50px;line-height:1}
.brand-sub{font-family:"Raleway",sans-serif;font-size:15px;color:var(--ink)}

/* hero */
.hero{left:0;top:54px;width:1200px;height:355px;background:radial-gradient(ellipse at 72% 40%,var(--blue) 0%,var(--blue-deep) 70%)}
.hero-photo{left:405px;top:75px;width:705px;height:334px;background:linear-gradient(180deg,rgba(220,230,240,.35),rgba(200,210,225,.55));border-radius:60px 60px 0 0}
.hero-title{left:117px;top:158px;font-family:"Raleway",sans-serif;font-weight:700;font-size:38px;line-height:44px;color:var(--white)}
.hero-title .dark{color:#111}
.hero-text{left:121px;top:253px;width:300px;font-size:14px;line-height:22px;color:var(--white)}
.band{left:0;top:409px;width:1200px;height:59px;background:repeating-linear-gradient(45deg,#333 0 2px,#2c2c2c 2px 4px)}
.btn-primary{left:120px;top:387px;width:185px;height:51px;background:linear-gradient(#d62027,#a80f14);border:2px solid #e6454a;border-radius:9px;box-shadow:0 2px 4px rgba(0,0,0,.5);color:var(--white);font-family:"Raleway",sans-serif;font-weight:700;font-size:22px;padding:10px 0 0 13px;z-index:2}
.btn-primary svg{position:absolute;left:154px;top:16px}

/* about */
.about{left:0;top:468px;width:1200px;height:305px;background:var(--light-bg)}
.about-rule{left:107px;top:566px;width:585px;height:4px;background:linear-gradient(90deg,#cfcfcf 0 30%,#e2e2e2 30%)}
.about-text{left:111px;top:585px;width:581px;font-size:12px;line-height:20px;text-align:justify;color:var(--body)}
.more-link{left:616px;top:716px;font-size:12px;font-style:italic;color:var(--red)}
.col-divider{left:716px;top:495px;width:1px;height:230px;background:#dadada}
.spec-title{left:738px;top:511px;font-family:"Raleway",sans-serif;font-weight:700;font-size:20px;color:var(--ink)}
.accent{color:var(--red)}
.spec-rule{left:737px;top:546px;width:340px;height:1px;background:var(--rule)}
.spec-rule::before{content:"";position:absolute;left:0;top:-1px;width:150px;height:4px;background:var(--rule)}
.spec-list{left:740px;top:565px;list-style:none}
.spec-list li{height:28px;font-size:13px;font-weight:700;color:var(--body);padding-left:17px;position:relative}
.spec-list li svg{position:absolute;left:0;top:4px}

/* services */
.services-shadow{left:0;top:773px;width:1200px;height:10px;background:linear-gradient(rgba(0,0,0,.08),transparent)}
.service-title{top:791px;font-family:"Raleway",sans-serif;font-weight:700;font-size:22px;color:var(--ink)}
.service-frame{top:831px;height:118px;background:var(--frame)}
.service-photo{position:absolute;left:9px;top:9px;right:9px;bottom:9px;border:1px solid #fff}
.service-text{top:963px;font-size:12px;line-height:18px;text-align:justify;color:var(--body)}
.dotted{top:818px;width:0;height:225px;border-left:1px dotted #bbb}

/* footer */
.footer{left:0;top:1070px;width:1200px;height:42px;background:#2a2a2a}
.copyright{left:107px;top:1083px;font-size:14px;color:var(--white)}
.social{top:1077px;width:29px;height:29px;border-radius:50%;background:linear-gradient(#f4f4f4,#cfcfcf)}
</style>
</head>
<body>

<header>
  <div class="abs top-bar"></div>
  <nav class="nav">
    <span class="active-tab"></span>
    <a href="#" style="left:532px">Home</a>
    <a href="#" style="left:634px">Our Value</a>
    <a href="#" style="left:762px">Our Services</a>
    <a href="#" style="left:890px">Our Expertise</a>
    <a href="#" style="left:1016px">Contact Us</a>
  </nav>
  <div class="abs logo-card">
    <div class="abs brand-name" style="left:17px;top:22px">Vornelix</div>
    <div class="abs brand-sub" style="left:62px;top:71px">IT Consulting Company</div>
  </div>
</header>

<section>
  <div class="abs hero"></div>
  <div class="abs hero-photo" role="img" aria-label="Photo of four business consultants seated around a glass meeting table with laptops"></div>
  <h1 class="abs hero-title"><span class="dark">Your Most Trusted</span> IT<br>Consultant</h1>
  <p class="abs hero-text">We are experienced, certified professionals who are experts at Information Technology (IT) consulting, solution design &amp; development, and training for medium-size businesses and large enterprises.</p>
  <div class="abs band"></div>
  <a class="abs btn-primary">More Details
    <svg width="22" height="18" viewBox="0 0 22 18"><path d="M2 2l7 7-7 7M11 2l7 7-7 7" fill="none" stroke="#fff" stroke-width="3.5"/></svg>
  </a>
</section>

<section>
  <div class="abs about"></div>
  <div class="abs brand-name" style="left:101px;top:492px">Vornelix</div>
  <div class="abs brand-sub" style="left:146px;top:540px">IT Consulting Company</div>
  <div class="abs about-rule"></div>
  <p class="abs about-text">Lorem ipsum dolor sit amet, consectetur adipiscing elit. Quisque dapibus accumsan orci, pretium eleifend arcu adipiscing eget. Fusce accumsan facilisis tincidunt. Phasellus tempor enim purus, vitae venenatis est. Ut imperdiet hendrerit pulvinar. Cras at tellus a enim condimentum mollis ut et tellus. Mauris dolor magna, elementum eu dictum eu, fermentum a nibh. Praesent ut dui lectus, vel lacinia sem. Praesent commodo malesuada urna, quis convallis risus dictum et. Nunc dapibus interdum libero, et semper eros auctor ac.</p>
  <a class="abs more-link">More Details <svg width="10" height="8" viewBox="0 0 10 8"><path d="M1 1l3 3-3 3M5 1l3 3-3 3" fill="none" stroke="#222" stroke-width="1.5"/></svg></a>

  <div class="abs col-divider"></div>
  <h2 class="abs spec-title"><span class="accent">Vornelix specializes</span> Technologies</h2>
  <div class="abs spec-rule"></div>
  <ul class="abs spec-list">
    <li><svg width="10" height="8" viewBox="0 0 10 8"><path d="M0 4h6M4 1l4 3-4 3" fill="none" stroke="#1f4f8f" stroke-width="1.6"/></svg>Corporate intranet portal and public web site</li>
    <li><svg width="10" height="8" viewBox="0 0 10 8"><path d="M0 4h6M4 1l4 3-4 3" fill="none" stroke="#1f4f8f" stroke-width="1.6"/></svg>Business intelligence solution</li>
    <li><svg width="10" height="8" viewBox="0 0 10 8"><path d="M0 4h6M4 1l4 3-4 3" fill="none" stroke="#1f4f8f" stroke-width="1.6"/></svg>Enterprise search solution</li>
    <li><svg width="10" height="8" viewBox="0 0 10 8"><path d="M0 4h6M4 1l4 3-4 3" fill="none" stroke="#1f4f8f" stroke-width="1.6"/></svg>Document and record management solution</li>
    <li><svg width="10" height="8" viewBox="0 0 10 8"><path d="M0 4h6M4 1l4 3-4 3" fill="none" stroke="#1f4f8f" stroke-width="1.6"/></svg>Business form and enterprise solution</li>
    <li><svg width="10" height="8" viewBox="0 0 10 8"><path d="M0 4h6M4 1l4 3-4 3" fill="none" stroke="#1f4f8f" stroke-width="1.6"/></svg>Knowledge management solution</li>
  </ul>
</section>

<section>
  <div class="abs services-shadow"></div>

  <h3 class="abs service-title" style="left:128px"><span class="accent">Consulting</span> Service</h3>
  <div class="abs service-frame" style="left:128px;width:256px">
    <div class="service-photo" role="img" aria-label="Overhead photo of a team meeting around a round white table" style="background:linear-gradient(135deg,#3d6a5c,#cfd3d6 50%,#6b7a86)"></div>
  </div>
  <p class="abs service-text" style="left:129px;width:255px">Vestibulum rutrum pharetra diam, eget dapibus leo vehicula ut. Fusce aliquam, odio eget adipiscing lobortis, nisl sapien placerat est...</p>

  <div class="abs dotted" style="left:426px"></div>

  <h3 class="abs service-title" style="left:468px"><span class="accent">Training</span> Service</h3>
  <div class="abs service-frame" style="left:467px;width:254px">
    <div class="service-photo" role="img" aria-label="Photo of people in silhouette in a bright training room" style="background:linear-gradient(180deg,#e8ecf4,#9aa6bd 60%,#2a3048)"></div>
  </div>
  <p class="abs service-text" style="left:471px;width:248px">Vestibulum rutrum pharetra diam, eget dapibus leo vehicula ut. Fusce aliquam, odio eget adipiscing lobortis, nisl sapien placerat est...</p>

  <div class="abs dotted" style="left:764px"></div>

  <h3 class="abs service-title" style="left:804px"><span class="accent">Solution</span> Service</h3>
  <div class="abs service-frame" style="left:804px;width:264px">
    <div class="service-photo" role="img" aria-label="Photo of hands typing on a keyboard" style="background:linear-gradient(90deg,#4fd0b4,#a9d7cf 50%,#e7b59a)"></div>
  </div>
  <p class="abs service-text" style="left:808px;width:257px">Vestibulum rutrum pharetra diam, eget dapibus leo vehicula ut. Fusce aliquam, odio eget adipiscing lobortis, nisl sapien placerat est...</p>
</section>

<footer>
  <div class="abs footer"></div>
  <p class="abs copyright">© Copyright vornelix-example.com Tax and financial solutions.</p>
  <span class="abs social" style="left:982px" aria-label="Social link"></span>
  <span class="abs social" style="left:1014px" aria-label="Social link"></span>
  <span class="abs social" style="left:1046px" aria-label="Social link"></span>
</footer>

</body>
</html>
```